Anesthesia Medical Practice Business Card

We need a business card to hand out to surgeons with my basic information. Something that stands out but is not over the top. The medical community is rather conservative. I'd like them to call me first when flipping through their rolodex of anesthesiologists. I'd like the card to communicate confidence, control, professionalism yet serenity. I don't want the card to be pricey to print.

he logo will be provided as a vector graphic in addition to a complete business card design including the logo

Rex Alba Tovell, M.D.
Board Certified Anesthesiologist

(555) 638-2175

rtovell@quillnet.example

Mailing Address:
48317 Pemberly Ave.
Suite 274-6583
Los Angeles, CA 90871

A logo that inegrates my initials perhaps
RT MD
My initials are RT and MD as in Medical Doctor

or
perhaps a physician in surgical mask and cap caring for a patient

Surgeons who need anesthesia services

Medical

• the logo will be provided as a vector graphic in addition to a complete business card design including the logo

Rex Alba Tovell, M.D.

(555) 638-2175

rtovell@quillnet.example

Mailing Address:
48317 Pemberly Ave.
Suite 274-6583
Los Angeles, CA 90871

• A logo that inegrates my initials perhaps
RT MD

or

```html
<!DOCTYPE html>
<html lang="en">
<head>
<meta charset="utf-8">
<title>Rex Alba Tovell, M.D. — Business Card</title>
<link rel="stylesheet" href="https://fonts.googleapis.com/css2?family=Gelasio:wght@400;700&display=swap">
<style>
  :root {
    --page-bg: #d9d9d9;
    --card-white: #ffffff;
    --panel-black: #000000;
    --text-white: #ffffff;
    --rule-grey: #bdbdbd;
    --accent-gold: #d9a016;
    --icon-ink: #1a1a1a;
  }
  * { margin: 0; padding: 0; box-sizing: border-box; }
  html, body {
    width: 1195px;
    height: 1200px;
    overflow: hidden;
    background: var(--page-bg);
    font-family: "Gelasio", Georgia, serif;
  }
  .business-card {
    position: absolute;
    left: 91px;
    top: 353px;
    width: 1010px;
    height: 579px;
    background: var(--card-white);
  }
  .card-panel {
    position: absolute;
    inset: 26px;
    background: var(--panel-black);
    border-radius: 14px;
    color: var(--text-white);
  }
  .practice-name {
    position: absolute;
    left: 0;
    right: 0;
    top: 72px;
    text-align: center;
    font-size: 80px;
    font-weight: 700;
    line-height: 1;
  }
  .rule {
    position: absolute;
    left: 90px;
    width: 798px;
    height: 1.5px;
    background: var(--rule-grey);
  }
  .rule--top { top: 213px; }
  .rule--bottom { top: 290px; }
  .title-row {
    position: absolute;
    left: 90px;
    width: 798px;
    top: 227px;
    height: 50px;
    font-size: 27px;
    line-height: 50px;
  }
  .doctor-name {
    position: absolute;
    left: 8px;
    font-weight: 700;
  }
  .title-divider {
    position: absolute;
    left: 367px;
    top: 1px;
    width: 1.5px;
    height: 48px;
    background: var(--rule-grey);
  }
  .specialty {
    position: absolute;
    right: 0;
    font-weight: 400;
  }
  .contact-item {
    position: absolute;
    display: flex;
    align-items: flex-start;
    font-size: 24px;
    line-height: 34px;
  }
  .contact-icon {
    flex: none;
    width: 40px;
    height: 40px;
    margin-right: 22px;
  }
  .contact-item--phone { left: 88px; top: 332px; }
  .contact-item--email { left: 88px; top: 399px; }
  .contact-item--address { left: 563px; top: 332px; }
  .contact-item--address .contact-icon { margin-right: 19px; }
  .contact-item--phone .contact-text,
  .contact-item--email .contact-text { margin-top: 3px; }
  .contact-item--address .contact-text { margin-top: 4px; }
</style>
</head>
<body>
  <section class="business-card">
    <div class="card-panel">
      <div class="practice-name">Tovell Anesthesia</div>
      <div class="rule rule--top"></div>
      <div class="title-row">
        <span class="doctor-name">Rex Alba Tovell, M.D.</span>
        <span class="title-divider"></span>
        <span class="specialty">Board Certified Anesthesiologist</span>
      </div>
      <div class="rule rule--bottom"></div>

      <div class="contact-item contact-item--phone">
        <svg class="contact-icon" viewBox="0 0 40 40" aria-hidden="true">
          <circle cx="20" cy="20" r="20" fill="var(--accent-gold)"/>
          <path d="M13 11.5c1-.9 2.2-.8 2.9.2l2 3c.5.8.3 1.8-.4 2.4l-1.2 1c.9 2.2 2.6 4 4.8 5l1-1.2c.6-.7 1.6-.9 2.4-.4l3 2c1 .7 1.1 1.900.2 2.9l-1.1 1.2c-1.3 1.4-3.3 1.7-5 .9-4.6-2.1-8.3-5.8-10.4-10.4-.8-1.7-.5-3.7.9-5z" fill="none" stroke="var(--icon-ink)" stroke-width="1.8" stroke-linejoin="round"/>
        </svg>
        <span class="contact-text">(555) 638-2175</span>
      </div>

      <div class="contact-item contact-item--email">
        <svg class="contact-icon" viewBox="0 0 40 40" aria-hidden="true">
          <circle cx="20" cy="20" r="20" fill="var(--accent-gold)"/>
          <rect x="11.5" y="14" width="17" height="12" rx="1" fill="none" stroke="var(--icon-ink)" stroke-width="1.8"/>
          <path d="M11.5 14.5l8.5 6.5 8.5-6.5" fill="none" stroke="var(--icon-ink)" stroke-width="1.8" stroke-linejoin="round"/>
        </svg>
        <span class="contact-text">rtovell@quillnet.example</span>
      </div>

      <div class="contact-item contact-item--address">
        <svg class="contact-icon" viewBox="0 0 40 40" aria-hidden="true">
          <circle cx="20" cy="20" r="20" fill="var(--accent-gold)"/>
          <path d="M11.5 19.5L20 12l8.5 7.5M14 17.5V28h12V17.5" fill="none" stroke="var(--icon-ink)" stroke-width="1.8" stroke-linejoin="round"/>
          <path d="M18 28v-5h4v5" fill="none" stroke="var(--icon-ink)" stroke-width="1.8"/>
        </svg>
        <span class="contact-text">48317 Pemberly Ave.<br>Suite 274-6583<br>Los Angeles, CA 90871</span>
      </div>
    </div>
  </section>
</body>
</html>
```